Flyer-Design für Unkrautbekämpfung
Sehr gute und nette Zusammenarbeit. Auch auf Änderungswünsche nach Beendigung der Contest-Phase wurde schnell eingegangen. Gerne wieder, sehr zu empfehlen!
Zielgruppe
Unkrautbekämpfung mit dem Heißwasser-Schaum-System. In Eigenleistung und Vermietung des Geräts.
Zielgruppe: Privatleute mit eigenem Grundstück, Landwirte, kleine Geschäfte (Restaurants, Läden mit Parkplatz etc.)
Aufgabenstellung
Link zur Website: www.beetglanz-service.net
Der Kreativität sind keine Grenzen gesetzt.
Bitte Vorder- und Rückseite designen. Auf der Rückseite können hauptsächlich Kontaktinformationen sein.

```html
<!DOCTYPE html>
<html lang="de">
<head>
<meta charset="utf-8">
<title>KLV Flyer – Vorder- und Rückseite</title>
<link rel="stylesheet" href="https://fonts.googleapis.com/css2?family=Raleway:ital,wght@0,400;0,500;0,700;0,800;1,400;1,500&display=swap">
<style>
:root{
  --bg:#ececec;
  --dark-green:#1f7a3d;
  --light-green:#7bc45a;
  --mid-green:#5fb446;
  --blue:#0d5089;
  --text:#3b3b3b;
  --white:#ffffff;
}
*{margin:0;padding:0;box-sizing:border-box}
html,body{width:1200px;height:656px;overflow:hidden;background:var(--bg);font-family:'Raleway',sans-serif}
.stage{position:relative;width:1200px;height:656px}
.flyer{position:absolute;width:601px;height:848px;background:var(--white);overflow:hidden;transform:scale(0.656);transform-origin:0 0;box-shadow:0 18px 22px rgba(0,0,0,.12)}
.flyer--front{left:164px;top:34px}
.flyer--back{left:666px;top:35px}
.abs{position:absolute}
.waves{position:absolute;left:0;top:0;width:601px;height:848px}
.brand{display:flex;align-items:center;gap:10px}
.brand__mark{width:44px;height:44px;background:var(--dark-green)}
.brand__name{font-weight:500;color:var(--dark-green);font-size:19px;line-height:1}
.brand__line{font-size:12.5px;color:#1c2a44;font-weight:500;margin-top:6px}
.photo{position:absolute}
.photo-label{position:absolute;background:rgba(123,196,90,.9);color:var(--white);font-style:italic;font-size:23px;padding:0 12px;border-radius:6px;line-height:28px}
.headline{font-weight:800;color:var(--dark-green);font-size:32px;line-height:29px}
.subline{color:var(--light-green);font-size:19.5px;font-weight:500}
.band-title{color:var(--white);font-weight:800;font-size:23px;transform:rotate(2deg);white-space:nowrap}
.checks{list-style:none}
.checks li{display:flex;align-items:center;gap:14px;font-style:italic;font-size:24px;color:var(--text);height:36.5px;white-space:nowrap}
.body-copy{font-size:14px;line-height:24.5px;color:var(--text);text-align:justify;width:346px}
.url{font-weight:800;color:var(--dark-green);font-size:26px;display:flex;align-items:center;gap:8px;white-space:nowrap}
.tagline{color:var(--white);font-size:12.5px;white-space:nowrap}
.speech{border:2px solid var(--white);color:var(--white);font-size:19px;font-weight:500;line-height:21px;padding:10px 9px;width:105px}
.cta{font-weight:800;color:var(--dark-green);font-size:31px;line-height:30px}
.contact{font-size:14px;font-style:italic;color:#2a2a2a;line-height:18px}
.contact b{font-style:normal;font-weight:500;color:var(--light-green)}
.contact-row{display:flex;gap:12px;align-items:flex-start}
.footer-info{color:var(--white);font-size:12.5px;font-weight:500;line-height:14px}
</style>
</head>
<body>
<div class="stage">

  <!-- Vorderseite -->
  <section class="flyer flyer--front">
    <svg class="waves" viewBox="0 0 601 848" aria-hidden="true">
      <rect x="0" y="0" width="601" height="8" fill="var(--light-green)"/>
      <path d="M0 205 C200 175 400 150 601 110 L601 150 C400 190 200 220 0 250Z" fill="var(--light-green)"/>
      <path d="M0 275 C200 240 400 225 601 185 L601 225 C400 260 200 285 0 320Z" fill="var(--dark-green)"/>
    </svg>

    <div class="photo" style="left:53px;top:97px;width:224px;height:190px;background:linear-gradient(160deg,#6d7a5a,#4d5a3f 60%,#7a8a5f)" role="img" aria-label="Foto: Pflasterweg mit Unkraut vor der Behandlung"></div>
    <div class="photo" style="left:325px;top:97px;width:224px;height:150px;background:linear-gradient(160deg,#5a5e5a,#2e322e 60%,#4a4f47)" role="img" aria-label="Foto: gereinigter Pflasterweg nach der Behandlung"></div>

    <svg class="waves" viewBox="0 0 601 848" aria-hidden="true">
      <path d="M0 330 C60 270 250 240 601 228 L601 258 C250 264 60 300 0 380Z" fill="var(--light-green)"/>
      <path d="M0 380 C60 300 250 264 601 258 L601 848 L0 848Z" fill="var(--white)"/>
      <path d="M0 490 C70 412 250 394 601 382 L601 442 C300 438 100 440 0 520Z" fill="var(--dark-green)"/>
      <path d="M0 640 C60 700 160 720 300 718 C420 716 520 710 601 712 L601 775 C450 770 300 770 200 780 C100 790 40 770 0 760Z" fill="var(--blue)"/>
      <path d="M0 785 C120 810 300 775 601 775 L601 848 L0 848Z" fill="var(--light-green)"/>
    </svg>

    <div class="photo-label" style="left:113px;top:148px">Vorher</div>
    <div class="photo-label" style="left:373px;top:148px">Nachher</div>

    <div class="abs brand" style="left:180px;top:26px">
      <div class="brand__mark"></div>
      <div><div class="brand__name">KLV</div><div class="brand__line">Biologische Unkrautvernichtung</div></div>
    </div>
    <div class="abs" style="left:470px;top:22px;width:104px;height:104px;border-radius:50%;background:var(--mid-green)" role="img" aria-label="Siegel"></div>

    <div class="abs headline" style="left:142px;top:290px">Unkrautbekämpfung<br>&amp; Flächenpflege</div>
    <div class="abs subline" style="left:142px;top:356px">Heißwasser-/Ökoschaum-Verfahren</div>
    <div class="abs band-title" style="left:212px;top:400px">Ökologie und Umwelt</div>

    <ul class="abs checks" style="left:135px;top:450px">
      <li><svg width="30" height="30" viewBox="0 0 30 30"><path d="M3 16 L11 27 L28 2" fill="none" stroke="var(--dark-green)" stroke-width="4"/></svg>100% biologisch abbaubar</li>
      <li><svg width="30" height="30" viewBox="0 0 30 30"><path d="M3 16 L11 27 L28 2" fill="none" stroke="var(--dark-green)" stroke-width="4"/></svg>umweltfreundlich</li>
      <li><svg width="30" height="30" viewBox="0 0 30 30"><path d="M3 16 L11 27 L28 2" fill="none" stroke="var(--dark-green)" stroke-width="4"/></svg>nicht gesundheitsschädlich</li>
      <li><svg width="30" height="30" viewBox="0 0 30 30"><path d="M3 16 L11 27 L28 2" fill="none" stroke="var(--dark-green)" stroke-width="4"/></svg>optimale Denkmalpflege</li>
    </ul>

    <p class="abs body-copy" style="left:129px;top:604px">Mit dem Heißwasser- /Heißwasser-Schaumverfahren wird nachhaltig Unkraut unter strikter Beachtung des Pflanzenschutzgesetzes umweltfreundlich, effizient und rein ökologisch beseitigt.</p>

    <div class="abs" style="left:545px;top:578px;width:56px;height:142px;background:var(--mid-green)" role="img" aria-label="Illustration: Tannen"></div>

    <div class="abs url" style="left:148px;top:790px">
      <svg width="28" height="28" viewBox="0 0 28 28"><g fill="none" stroke="var(--white)" stroke-width="2"><circle cx="14" cy="14" r="12"/><ellipse cx="14" cy="14" rx="5" ry="12"/><path d="M2 14H26M4 8H24M4 20H24"/></g></svg>
      www.beetglanz-service.net
    </div>
    <div class="abs tagline" style="left:185px;top:820px">leistungsstark • wirtschaftlich günstig • ökologisch</div>
  </section>

  <!-- Rückseite -->
  <section class="flyer flyer--back">
    <div class="photo" style="left:0;top:0;width:601px;height:400px;background:linear-gradient(135deg,#8aa36d,#4f7a3c 50%,#6e8f58)" role="img" aria-label="Foto: Unkrautbehandlung mit Heißschaum im Beet"></div>
    <div class="abs speech" style="left:41px;top:26px">Unkraut ohne Gift im Griff</div>

    <svg class="waves" viewBox="0 0 601 848" aria-hidden="true">
      <path d="M0 280 C180 330 430 270 601 330 L601 848 L0 848Z" fill="var(--dark-green)"/>
      <path d="M0 315 C180 360 430 300 601 360 L601 848 L0 848Z" fill="var(--white)"/>
      <path d="M0 330 C180 375 430 320 601 385 L601 848 L0 848Z" fill="var(--light-green)"/>
      <path d="M0 350 C180 395 430 345 601 420 L601 848 L0 848Z" fill="var(--white)"/>
      <path d="M0 375 C200 410 430 380 601 460 L601 470 C430 400 200 420 0 390Z" fill="var(--light-green)"/>
      <path d="M0 720 C200 700 420 760 601 650 L601 848 L0 848Z" fill="var(--light-green)"/>
      <path d="M0 775 C220 730 420 800 601 720 L601 848 L0 848Z" fill="var(--white)"/>
      <path d="M0 800 C220 760 420 820 601 760 L601 848 L0 848Z" fill="var(--blue)"/>
    </svg>

    <div class="abs brand" style="left:68px;top:428px">
      <div class="brand__mark"></div>
      <div><div class="brand__name">KLV</div><div class="brand__line">Biologische Unkrautvernichtung</div></div>
    </div>
    <div class="abs cta" style="left:72px;top:500px">Sprechen Sie<br>uns einfach an:</div>

    <div class="abs" style="left:352px;top:452px;width:250px;height:212px;background:linear-gradient(135deg,#e7f3e1,#d4e8cc)" role="img" aria-label="Illustration: Person bei der Unkrautbehandlung mit Schaumlanze"></div>
    <div class="abs" style="left:0;top:580px;width:55px;height:142px;background:var(--mid-green)" role="img" aria-label="Illustration: Tannen"></div>

    <div class="abs contact" style="left:157px;top:600px">
      <div class="contact-row"><svg width="12" height="16" viewBox="0 0 12 16"><rect x="1" y="1" width="10" height="14" rx="1.5" fill="none" stroke="var(--dark-green)" stroke-width="1.6"/></svg><div><b>Festnetz :</b> 05123 - 4567<br><b>Mobil:</b> 0151-2345678</div></div>
      <div class="contact-row" style="margin-top:18px;margin-left:-2px"><svg width="15" height="12" viewBox="0 0 15 12"><rect x="1" y="1" width="13" height="10" fill="none" stroke="var(--dark-green)" stroke-width="1.4"/><path d="M1 1 L7.5 7 L14 1" fill="none" stroke="var(--dark-green)" stroke-width="1.4"/></svg><div>info@beetglanz-service.net</div></div>
    </div>

    <div class="abs footer-info" style="left:134px;top:798px">KLV - Biologische Unkrautvernichtung<br>Inh. Torben Hallweg</div>
    <div class="abs footer-info" style="left:388px;top:798px">Lindenweg 12<br>31600 Musterfeld</div>
  </section>

</div>
</body>
</html>
```